Volt'r Electrical Business Card Design

FRONT OF CARD: should highlight the company logo ( please use image attached) and in small font in the bottom corner must have REC 48197

BACK OF CARD : Company logo at the top, underneath the logo have my name Owen Marsh under my name in smaller font Qualified Electrician.
Details to also include are Mobile: 0438715209 E-mail: voltrelectrical@mailbox-example.net

Front and back of card please try to use similar colours as used in the logo. (Blues, greys, black and white)

The logo was created on this website so if you need a different file type of the logo please notify me.

Thanks, Owen

Industry/Entity Type

Business

Contact Information for Business Card

Details are in project description.

Colors
3176b5

Requirements
Must have
• Company logo and contact details

```html
<!DOCTYPE html>
<html lang="en">
<head>
<meta charset="utf-8">
<title>Volt'r Electrical — Business Card Front</title>
<link href="https://fonts.googleapis.com/css2?family=Orbitron:wght@500&display=swap" rel="stylesheet">
<style>
  :root {
    --page: #ffffff;
    --navy-top: #08355a;
    --navy-bottom: #021b40;
    --glow: #4dd6ef;
    --ink: #0a3152;
    --accent: #5ad8f2;
    --divider: #2b5a86;
  }
  html, body {
    margin: 0;
    padding: 0;
    width: 1200px;
    height: 752px;
    overflow: hidden;
    background: var(--page);
  }
  .card {
    position: relative;
    width: 1200px;
    height: 752px;
  }
  .card-art {
    position: absolute;
    inset: 0;
  }
  .brand {
    position: absolute;
    left: 0;
    right: 0;
    top: 312px;
    margin: 0;
    display: flex;
    justify-content: center;
    align-items: center;
    gap: 22px;
    font-family: "Orbitron", sans-serif;
    font-weight: 500;
    font-size: 50px;
    line-height: 1;
    letter-spacing: 0;
    color: var(--ink);
  }
  .brand-dot {
    width: 22px;
    height: 22px;
    border-radius: 50%;
    background: var(--ink);
    flex: none;
  }
  .licence {
    position: absolute;
    left: 949px;
    top: 676px;
    margin: 0;
    font-family: "Orbitron", sans-serif;
    font-weight: 500;
    font-size: 27px;
    letter-spacing: 2px;
    color: var(--accent);
  }
</style>
</head>
<body>
<main class="card">
  <svg class="card-art" width="1200" height="752" viewBox="0 0 1200 752" aria-hidden="true">
    <defs>
      <linearGradient id="top-band-fill" x1="0" y1="0" x2="0" y2="1">
        <stop offset="0" stop-color="#08355a"/>
        <stop offset="0.68" stop-color="#08355a"/>
        <stop offset="0.86" stop-color="#1a6d96"/>
        <stop offset="1" stop-color="#4dd6ef"/>
      </linearGradient>
      <linearGradient id="bottom-band-fill" x1="0" y1="0" x2="0" y2="1">
        <stop offset="0" stop-color="#4dd6ef"/>
        <stop offset="0.1" stop-color="#1a6d96"/>
        <stop offset="0.26" stop-color="#021b40"/>
        <stop offset="1" stop-color="#021b40"/>
      </linearGradient>
    </defs>
    <path class="top-band" d="M19 0 H1180 V193 Q600 295 19 193 Z" fill="url(#top-band-fill)"/>
    <path class="bottom-band" d="M19 752 V490 Q600 378 1180 490 V752 Z" fill="url(#bottom-band-fill)"/>
    <line class="licence-divider" x1="920" y1="650" x2="920" y2="752" stroke="#2b5a86" stroke-width="1.5"/>
  </svg>

  <h1 class="brand">
    <span class="brand-dot" aria-hidden="true"></span>
    <span class="brand-name">Volt'r Electrical</span>
  </h1>

  <p class="licence">REC 48197</p>
</main>
</body>
</html>
```